Motivational Poster Design Project

I would like to create a poster with some of my favorite quotes to hang in my office. I did a similar project in 2012 and I've uploaded the top 2 designs so you can get a better idea of what I'm looking for. I will provide feedback on your design within 24 hours of receiving it.

The poster must contain the following quotes:

"You’re only given a little spark of madness. You mustn’t lose it.”
- Dorian Halbrook

“The most contrarian thing of all is not to oppose the crowd but to think for yourself.”
- Marcus Vell

"I constantly see people rise in life who are not the smartest, sometimes not even the most diligent, but they are learning machines. They go to bed every night a little wiser than they were when they got up and boy does that help, particularly when you have a long run ahead of you."
- Walter Brisco

“In theory, there’s no difference between theory and practice. But, in practice, there is.”
- Piet R. K. Ter Wolvenkamp

"At the end of the day, a reactionary life is a normal life. One thing is consistent in every remarkable person: they decide to do something remarkable. Don’t let the world choose who you become."
- Ravindra Kolpe

“It usually takes 3-4 months to try enough that you can do a proper 80/20 analysis, then two months to design systems to scale what *is* working.”
-Gus Ambery

“Authority is 20 percent given, 80 percent taken.”
- Harold Quimsby

“Your actions are consistent with the way the world occurs to you.”
- Anselm Grottke

Project Deadline Extended
Reason: I am going to be travelling with no access to internet until January 5th, 2015. I am extending the project deadline until 12/31/14 and I'll make a final decision during the 1st week of January.

Target Market(s)

Personal Project

Industry/Entity Type

Learning

Requirements
Must have
• The poster will be 24" high x 36" long and printed on canvas, so the image you create needs to have a resolution of at least 2700 x 3900.
Nice to have
• I don't have an exact vision for how the poster should look, so I am totally open to you using your creativity to develop, arrange and present the content as you'd like.
• That said, I would like an image (photo or posterized image) of the person being quoted along with each quote. I do not have specific images that I would like you to use, so you will need to find the images on your own. The images don't need to be perfect... I am more interested in the poster relating the essence of the quotes and the people being quoted than I am in perfect photographic images of the people being quoted.

```html
<!DOCTYPE html>
<html lang="en">
<head>
<meta charset="utf-8">
<title>Favourite Quotes Poster</title>
<link rel="stylesheet" href="https://fonts.googleapis.com/css2?family=Roboto:wght@300;400;500;700;900&family=Open+Sans:wght@400;600;700;800&display=swap">
<style>
  :root {
    --paper: #ffffff;
    --grey: #7b7b7b;
    --ink: #1d1d1b;
    --navy: #27338f;
    --sky: #1a74bb;
    --violet: #8a2c8e;
    --lilac: #9a58a9;
    --lime: #7dc242;
    --green: #1f9a48;
    --teal: #2ab3a3;
    --tan: #c9a26d;
    --brown: #8a5a2e;
    --red: #e3222a;
    --azure: #1c75bf;
    --crimson: #c2272d;
    --orange: #f26a1e;
    --tone-purple: #a68bc2;
    --tone-blue: #9fc4e6;
    --tone-green: #6fc59a;
    --tone-brown: #a88466;
    --tone-salmon: #f39b7e;
    --tone-gold: #f8c07a;
  }
  * { margin: 0; padding: 0; box-sizing: border-box; }
  html, body { width: 904px; height: 1200px; overflow: hidden; background: var(--paper); }
  .poster { position: relative; width: 904px; height: 1200px; overflow: hidden; font-family: "Roboto", Arial, sans-serif; color: var(--grey); }
  .ornament { position: absolute; inset: 0; }
  .line { position: absolute; white-space: nowrap; line-height: 1; font-weight: 700; }
  .credit { position: absolute; white-space: nowrap; font-size: 11px; color: var(--grey); font-weight: 400; }
  .sans { font-family: "Open Sans", Arial, sans-serif; }

  .spark .lead { font-size: 24px; }
  .spark .mark { color: var(--red); font-size: 32px; font-weight: 900; }
  .spark .big { color: var(--navy); }
  .spark .end { color: var(--sky); }

  .contrarian .lead { font-size: 19px; }
  .contrarian .mark { color: var(--violet); }
  .contrarian .soft { color: var(--lilac); font-weight: 300; }
  .contrarian .strong { color: var(--violet); }

  .learning .line { font-size: 15.5px; }
  .learning .lime { color: var(--lime); }
  .learning .green { color: var(--green); }
  .learning .teal { color: var(--teal); font-weight: 600; }

  .theory .lt { color: var(--tan); }
  .theory .dk { color: var(--brown); }

  .remark .line { font-size: 15px; }
  .remark .blue { color: var(--azure); }
  .remark .red { color: var(--red); }

  .systems .line { font-size: 17px; font-weight: 500; }
  .systems .hot { color: var(--crimson); font-weight: 900; }

  .authority .line { left: 610px; width: 200px; text-align: center; color: var(--azure); }
  .authority .head { color: var(--ink); font-weight: 500; }
  .authority .num { font-size: 46px; font-weight: 900; }
  .authority .sub { font-size: 20px; font-weight: 400; }

  .actions .line { color: var(--orange); }
  .actions .big { font-size: 26px; }
  .actions .tiny { font-size: 10px; font-weight: 400; }
</style>
</head>
<body>
<main class="poster">

  <svg class="ornament" width="904" height="1200" viewBox="0 0 904 1200" role="img" aria-label="Scattered translucent geometric ornament in soft purple, blue, green, brown, salmon and gold tones">
    <defs>
      <radialGradient id="glow-purple"><stop offset="0" stop-color="var(--tone-purple)" stop-opacity="0.55"/><stop offset="1" stop-color="var(--tone-purple)" stop-opacity="0"/></radialGradient>
      <radialGradient id="glow-blue"><stop offset="0" stop-color="var(--tone-blue)" stop-opacity="0.55"/><stop offset="1" stop-color="var(--tone-blue)" stop-opacity="0"/></radialGradient>
      <radialGradient id="glow-green"><stop offset="0" stop-color="var(--tone-green)" stop-opacity="0.5"/><stop offset="1" stop-color="var(--tone-green)" stop-opacity="0"/></radialGradient>
      <radialGradient id="glow-brown"><stop offset="0" stop-color="var(--tone-brown)" stop-opacity="0.55"/><stop offset="1" stop-color="var(--tone-brown)" stop-opacity="0"/></radialGradient>
      <radialGradient id="glow-salmon"><stop offset="0" stop-color="var(--tone-salmon)" stop-opacity="0.55"/><stop offset="1" stop-color="var(--tone-salmon)" stop-opacity="0"/></radialGradient>
      <radialGradient id="glow-gold"><stop offset="0" stop-color="var(--tone-gold)" stop-opacity="0.55"/><stop offset="1" stop-color="var(--tone-gold)" stop-opacity="0"/></radialGradient>
    </defs>
    <ellipse cx="105" cy="40" rx="70" ry="65" fill="url(#glow-purple)"/>
    <ellipse cx="45" cy="225" rx="90" ry="85" fill="url(#glow-purple)"/>
    <ellipse cx="770" cy="50" rx="95" ry="80" fill="url(#glow-blue)"/>
    <ellipse cx="860" cy="265" rx="85" ry="80" fill="url(#glow-blue)"/>
    <ellipse cx="185" cy="345" rx="45" ry="40" fill="url(#glow-green)"/>
    <ellipse cx="730" cy="570" rx="55" ry="40" fill="url(#glow-green)"/>
    <ellipse cx="40" cy="630" rx="75" ry="75" fill="url(#glow-brown)"/>
    <ellipse cx="710" cy="830" rx="35" ry="35" fill="url(#glow-blue)"/>
    <ellipse cx="525" cy="905" rx="38" ry="32" fill="url(#glow-blue)"/>
    <ellipse cx="40" cy="1085" rx="80" ry="75" fill="url(#glow-salmon)"/>
    <ellipse cx="340" cy="1180" rx="70" ry="55" fill="url(#glow-gold)"/>
    <ellipse cx="840" cy="1110" rx="110" ry="100" fill="url(#glow-green)"/>
  </svg>

  <section class="quote spark">
    <div class="line lead" style="left:192px;top:50px"><span class="mark">"</span>You're only given a</div>
    <div class="line big" style="left:310px;top:80px;font-size:34px">little spark</div>
    <div class="line big" style="left:392px;top:114px;font-size:16px">of</div>
    <div class="line big" style="left:345px;top:124px;font-size:36px">madness.</div>
    <div class="line end" style="left:274px;top:153px;font-size:42px">You mustn't lose it.<span class="mark">"</span></div>
    <div class="credit" style="left:585px;top:196px">- Dorian Halbrook</div>
  </section>

  <section class="quote contrarian">
    <div class="line lead" style="left:218px;top:240px"><span class="mark">“</span>The most contrarian thing</div>
    <div class="line lead" style="left:235px;top:264px">of all is not to</div>
    <div class="line soft" style="left:265px;top:278px;font-size:30px">oppose the</div>
    <div class="line strong" style="left:320px;top:294px;font-size:38px">crowd</div>
    <div class="line lead" style="left:458px;top:312px;font-size:17px">but to</div>
    <div class="line strong" style="left:520px;top:312px;font-size:28px">think for</div>
    <div class="line strong" style="left:590px;top:334px;font-size:28px">yourself."</div>
    <div class="credit" style="left:730px;top:362px;font-size:10px">- Marcus Vell</div>
  </section>

  <section class="quote learning sans">
    <div class="line" style="left:155px;top:398px">"I constantly see <span class="lime" style="font-size:36px">people rise</span> in <span class="lime" style="font-size:36px">life</span> who are not the</div>
    <div class="line" style="left:155px;top:430px"><span class="green" style="font-size:28px">smartest</span>, sometimes not even the <span class="green" style="font-size:28px">most diligent</span>, but</div>
    <div class="line" style="left:155px;top:458px">they are <span class="teal">learning machines.</span> They go to bed every night a</div>
    <div class="line lime" style="left:442px;top:472px;font-size:38px">little wiser</div>
    <div class="line" style="left:155px;top:510px">than they were when they got up and boy does that help, particularly</div>
    <div class="line" style="left:155px;top:529px">when you have a long run ahead of you."</div>
    <div class="credit" style="left:510px;top:546px;font-size:10px">- Walter Brisco</div>
  </section>

  <section class="quote theory">
    <div class="line lt" style="left:182px;top:602px;font-size:20px">“In theory, there's <span style="font-size:34px">no difference</span> between</div>
    <div class="line" style="left:220px;top:632px;font-size:46px"><span class="dk">theory</span> <span class="lt" style="font-size:28px;font-weight:400">and</span> <span class="dk">practice</span><span class="lt">.</span></div>
    <div class="line lt" style="left:468px;top:670px;font-size:13px;font-weight:400">But,</div>
    <div class="line lt" style="left:508px;top:676px;font-size:32px">in practice,</div>
    <div class="line dk" style="left:585px;top:705px;font-size:48px">there is.<span class="lt" style="font-size:20px">”</span></div>
    <div class="credit" style="left:612px;top:748px">- Piet R. K. Ter Wolvenkamp</div>
  </section>

  <section class="quote remark">
    <div class="line" style="left:62px;top:730px">"At the end of the day, a</div>
    <div class="line" style="left:110px;top:742px"><span class="blue" style="font-size:26px">reactionary life</span> is a</div>
    <div class="line red" style="left:235px;top:762px;font-size:32px">normal life.</div>
    <div class="line" style="left:62px;top:788px">One thing is consistent in every <span class="blue" style="font-size:24px">remarkable person:</span></div>
    <div class="line" style="left:210px;top:810px">they decide to do something <span class="red" style="font-size:24px">remarkable</span>.</div>
    <div class="line" style="left:232px;top:835px">Don't let the world choose who you become."</div>
    <div class="credit" style="left:455px;top:852px;font-size:10px">- Ravindra Kolpe</div>
  </section>

  <section class="quote systems">
    <div class="line" style="left:58px;top:928px">“It usually takes <span class="hot" style="font-size:34px">3-4</span> months to try enough</div>
    <div class="line" style="left:160px;top:962px">that you can do a proper <span class="hot" style="font-size:24px">80/20</span> analysis,</div>
    <div class="line" style="left:160px;top:985px">then two months to design systems to scale</div>
    <div class="line hot" style="left:160px;top:998px;font-size:36px">what *is* working.<span style="color:var(--grey)">"</span></div>
    <div class="credit" style="left:538px;top:1030px;font-size:10px">-Gus Ambery</div>
  </section>

  <section class="quote authority">
    <div class="line head" style="top:888px;font-size:20px">“Authority is</div>
    <div class="line num" style="top:916px">20</div>
    <div class="line sub" style="top:960px">percent given,</div>
    <div class="line num" style="top:984px">80</div>
    <div class="line sub" style="top:1026px">percent taken.<span style="color:var(--ink)">”</span></div>
    <div class="credit" style="left:705px;top:1050px;font-size:10px">- Harold Quimsby</div>
  </section>

  <section class="quote actions">
    <div class="line big" style="left:280px;top:1070px">“Your actions</div>
    <div class="line tiny" style="left:296px;top:1098px">are consistent with the way the</div>
    <div class="line big" style="left:436px;top:1100px">world occurs <span class="tiny">to</span></div>
    <div class="line big" style="left:568px;top:1126px">you.”</div>
    <div class="credit" style="left:622px;top:1137px;font-size:10px">-Anselm Grottke</div>
  </section>

</main>
</body>
</html>
```